Business Card Design

I need a Business Card that will catch the attention that will not get thrown in a Drawer. I have 23 companies I use for Auto, Home, Life, and Business Insurance. I make sure that people have the best coverage for the $ spent.

Industry/Entity Type

Business

Contact Information for Business Card

Dorlin Insurance Agency, Inc., Marcus Helgren, 4375 West Tamber Lane Corvale, Westmark 45192 555-281-7496, www.dorlinagency.example, Friendspace, WorkLinker, Circlenet

```html
<!DOCTYPE html>
<html lang="en">
<head>
<meta charset="utf-8">
<title>Dorlin Insurance Agency – Business Card</title>
<link rel="stylesheet" href="https://fonts.googleapis.com/css2?family=Didact+Gothic&family=Delius&display=swap">
<style>
  :root {
    --paper: #ffffff;
    --navy: #34479c;
    --teal: #52c2b6;
    --orange: #f29b33;
    --green: #6cc270;
    --pink: #e2439c;
    --ink: #111111;
    --glow-orange: #ffc48a;
    --glow-pink: #ff8fcf;
    --glow-green: #a6e39d;
    --glow-teal: #96e0d6;
  }
  html, body {
    margin: 0;
    padding: 0;
    overflow: hidden;
    background: var(--paper);
  }
  .card {
    position: relative;
    width: 1200px;
    height: 702px;
    background: var(--paper);
    overflow: hidden;
  }
  .accent-bars {
    position: absolute;
    inset: 0;
  }
  .agency-name {
    position: absolute;
    top: 0;
    left: 0;
    margin: 0;
    font-family: "Didact Gothic", "Century Gothic", sans-serif;
    font-weight: 400;
    font-size: 40px;
    line-height: 1;
    color: var(--navy);
  }
  .agency-name .word {
    position: absolute;
    top: 206px;
    white-space: nowrap;
  }
  .word-dorlin { left: 258px; }
  .word-insurance { left: 446px; }
  .word-agency { left: 640px; }

  .contact {
    font-family: "Delius", "Comic Sans MS", cursive;
    position: absolute;
    margin: 0;
    white-space: nowrap;
  }
  .person-name {
    left: 644px;
    top: 314px;
    font-size: 25px;
    letter-spacing: 1.5px;
    color: var(--teal);
  }
  .address {
    left: 642px;
    top: 370px;
    font-size: 17px;
    font-weight: 700;
    letter-spacing: 1.2px;
    line-height: 25px;
    color: var(--orange);
    font-style: normal;
  }
  .phone-line {
    left: 323px;
    top: 424px;
    font-size: 19px;
    font-weight: 700;
    letter-spacing: 1.3px;
    color: var(--green);
  }
  .web {
    left: 380px;
    top: 526px;
    font-size: 14.5px;
    font-weight: 700;
    letter-spacing: 1px;
    color: var(--ink);
  }
  .social {
    left: 606px;
    top: 524px;
    font-size: 16px;
    font-weight: 700;
    letter-spacing: 1px;
    color: var(--pink);
  }
</style>
</head>
<body>
<main class="card">
  <svg class="accent-bars" width="1200" height="702" viewBox="0 0 1200 702" aria-hidden="true">
    <defs>
      <filter id="soft-glow" x="-200%" y="-5%" width="500%" height="110%">
        <feGaussianBlur stdDeviation="1.8"/>
      </filter>
    </defs>
    <g class="glows" filter="url(#soft-glow)">
      <rect x="436" y="186" width="7" height="217" fill="var(--glow-orange)"/>
      <rect x="265" y="343" width="7" height="216" fill="var(--glow-pink)"/>
      <rect x="622" y="293" width="7" height="217" fill="var(--glow-green)"/>
      <rect x="932" y="145" width="7" height="217" fill="var(--glow-teal)"/>
    </g>
    <g class="bars" fill="var(--navy)">
      <rect x="432" y="187" width="3.5" height="215"/>
      <rect x="261" y="344" width="3.5" height="214"/>
      <rect x="618" y="294" width="3.5" height="215"/>
      <rect x="928" y="146" width="3.5" height="215"/>
    </g>
  </svg>

  <h1 class="agency-name" aria-label="Dorlin Insurance Agency, Inc">
    <span class="word word-dorlin">Dorlin</span>
    <span class="word word-insurance">Insurance</span>
    <span class="word word-agency">Agency, Inc</span>
  </h1>

  <p class="contact person-name">Marcus Helgren</p>
  <address class="contact address">4375 West Tamber Lane,<br>Corvale, Westmark</address>
  <p class="contact phone-line">45192&nbsp; 555-281-7496</p>
  <p class="contact web">www.dorlinagency.example</p>
  <p class="contact social">Friendspace, WorkLinker, Circlenet</p>
</main>
</body>
</html>
```